Natural Skincare Product Labels Design

We are looking for a designer to create elegant but quirky, functional product labels for our natural skincare range.
The labels must reflect our brand’s values of simplicity, luxury, and the natural, handmade essence of our products.
https://www.instagram.com/tolvarenskincare
1. Key Details
Packaging Dimensions
Container Types: Transparent jars.
Sizes for Body Products:
Diameter: 64mm–68mm.
Heights: 80mm, 88mm, and 97mm (lid height: 15mm).
Sizes for Face Creams:
Diameter: 60mm.
Height: 50mm (lid height: 15mm).
Label Fit: For body products, ideally one label size to fit all jar sizes.
For the smaller face cream jars, a separate, tailored label is required.
2. Label Placement
Options include a wrapped-around label or a combination of wrapped-around and top-of-jar elements.
Transparent jars mean the label must leave space for the product to be visible (e.g., partial wrap or cutout areas).
3. Content Requirements
Product Name: Prominently displayed.
Ingredient List: Dedicated space required.
Disclaimer/Usage Instructions: Include space for this information.
4. Design Goals
Look & Feel: Simple, upmarket, and natural, with a handmade essence.
Logo Usage: Our logo is finalized and available in gold, black, and white variants. Use Josefin Bold font for the logo if adjustments are required.
Color Palette: Neutral tones (e.g., whites, blacks, golds) are preferred, with flexibility for subtle pops of color tied to each product’s main ingredient.
5. Imagery
Open to including images and colours (e.g., botanical illustrations) that highlight the main ingredient (e.g., coffee beans, turmeric root, or honeycomb). Also open to labels having a prominent colour to tie it in to the main ingredient.
Alternatively, no images can also work for a clean design.
6. Current Design Context
Our temporary design features gold leaf on top and a simple handmade side label. We’re seeking to elevate this to a more polished, cohesive design.
7. Product Line
- Body Products (Larger Jars)
Mivo Body Butter
Key Ingredients: Guarana & Cupuaçu butter (inspired by Brazil).
Note: “Mivo” is slang for “bum.”
Manuka Honey Body Butter
Key Ingredients: Manuka honey (from New Zealand) & Cupuaçu butter.
Coffee Body Scrub
Key Ingredients: Coffee and Demerara sugar.
Whipped Body Soap - Turmeric
Key Ingredients: Turmeric and Bentonite clay.
Whipped Body Soap - Banana
- Face Products (Smaller Jars)
Face Cream
Key Ingredients: Carrot Oil and Raspberry Oil.
Features natural UV protection.
Good Night Cream
Key Ingredients: Enriched with Magnesium.
Promotes relaxation and restful sleep.
8. Submission Guidelines
Flexibility: Design should allow for consistent branding across all products while accommodating the varying jar sizes and ingredient focus.
Material Considerations: Labels should complement the transparent jars and allow the product inside to remain partially visible.
Print Elements: Incorporating gold accents is a plus but should not overpower the design.
We’re excited to see your vision for a label that celebrates the natural beauty and high quality of our skincare range. Please include mockups to showcase the design in use, particularly on transparent jars of varying sizes.
women 20-50 years of age

```html
<!DOCTYPE html>
<html lang="en">
<head>
<meta charset="utf-8">
<title>Tolvaren Natural Skincare – Jar Labels</title>
<link rel="stylesheet" href="https://fonts.googleapis.com/css2?family=Josefin+Sans:wght@300;400&family=Montserrat:wght@400;500;600&display=swap">
<style>
  :root {
    --page-bg: #e8e8e8;
    --label-white: #ffffff;
    --ink: #111111;
    --ink-soft: #333333;
    --gold: #c4922f;
    --gold-light: #dcc08e;
    --purple: #c400ff;
    --purple-light: #db7af5;
    --rust: #ab4a19;
    --rust-light: #d39c82;
    --on-colour: #ffffff;
  }
  * { box-sizing: border-box; margin: 0; padding: 0; }
  html, body {
    width: 720px; height: 1200px; overflow: hidden;
    background: var(--page-bg);
    font-family: "Montserrat", Arial, sans-serif;
  }
  .label-sheet {
    position: relative; width: 720px; height: 1200px;
    display: flex; flex-direction: column; align-items: center;
    justify-content: center; gap: 44px;
  }
  .label {
    position: relative; width: 640px; height: 228px;
    background: var(--label-white); overflow: hidden;
  }
  .label--manuka { --accent: var(--gold);   --accent-light: var(--gold-light); }
  .label--mivo   { --accent: var(--purple); --accent-light: var(--purple-light); }
  .label--coffee { --accent: var(--rust);   --accent-light: var(--rust-light); }

  .label-bg { position: absolute; inset: 0; width: 100%; height: 100%; }
  .label-bg .panel { fill: var(--accent); }
  .label-bg .swoosh { fill: var(--accent-light); }

  .label-front {
    position: absolute; left: 48px; top: 0; width: 258px; height: 100%;
    text-align: center;
  }
  .brand-mark {
    position: absolute; left: 0; right: 0; top: 76px;
    display: flex; align-items: center; justify-content: center; gap: 9px;
  }
  .brand-dot { width: 9px; height: 9px; border-radius: 50%; background: var(--gold); }
  .brand-name {
    font-family: "Josefin Sans", Arial, sans-serif; font-weight: 300;
    font-size: 22px; letter-spacing: 5px; color: var(--gold); line-height: 1;
  }
  .brand-tagline {
    position: absolute; left: 0; right: 0; top: 107px;
    font-size: 6.5px; letter-spacing: 2px; color: var(--gold); font-weight: 500;
  }
  .product-band {
    position: absolute; left: 0; right: 0; top: 123px; height: 24px;
    background: var(--accent); color: var(--on-colour);
    font-size: 20px; font-weight: 500; line-height: 25px; letter-spacing: 0.5px;
  }
  .product-type {
    position: absolute; left: 0; right: 0; top: 148px;
    font-size: 20px; font-weight: 600; color: var(--ink); letter-spacing: 0.5px;
  }
  .product-keys {
    position: absolute; left: 0; right: 0; top: 183px;
    font-size: 11.5px; line-height: 15px; color: var(--ink-soft); letter-spacing: 0.3px;
  }

  .label-info {
    position: absolute; left: 380px; top: 24px; width: 226px;
    text-align: center; color: var(--on-colour);
    font-size: 11px; line-height: 12.8px;
  }
  .info-heading { font-weight: 600; font-size: 11px; letter-spacing: 0.3px; }
  .info-block + .info-block { margin-top: 8px; }
  .label--coffee .info-block + .info-block { margin-top: 20px; }

  .label-marks {
    position: absolute; left: 418px; top: 167px;
    display: flex; align-items: center; gap: 9px; color: var(--on-colour);
  }
  .volume { font-size: 9px; font-weight: 600; margin-right: 6px; }
  .open-jar-icon { width: 30px; height: 30px; }
  .cert-badge {
    width: 35px; height: 35px; border-radius: 50%;
    border: 2px solid var(--on-colour);
  }
</style>
</head>
<body>
<main class="label-sheet">

  <section class="label label--manuka">
    <svg class="label-bg" viewBox="0 0 1070 380" preserveAspectRatio="none" aria-hidden="true">
      <path class="swoosh" d="M525,90 C565,30 650,8 730,0 L700,8 C660,20 640,35 628,55 C605,95 625,160 592,232 C550,315 470,345 425,380 L385,380 C470,330 540,290 565,228 C595,160 570,110 588,70 C565,70 540,78 525,90 Z"/>
      <path class="panel" d="M730,0 L1070,0 L1070,380 L425,380 C490,335 570,300 605,225 C640,150 610,85 645,45 C670,15 700,6 730,0 Z"/>
    </svg>
    <div class="label-front">
      <div class="brand-mark"><span class="brand-dot"></span><span class="brand-name">TOLVAREN</span></div>
      <div class="brand-tagline">NATURAL SKINCARE</div>
      <div class="product-band">MANUKA HONEY</div>
      <div class="product-type">BODY BUTTER</div>
      <div class="product-keys">MANUKA HONEY<br>&amp; CUPUAÇU BUTTER</div>
    </div>
    <div class="label-info">
      <div class="info-block">
        <div class="info-heading">INGREDIENTS:</div>
        <p>Shea butter, cocoa butter, manuka honey, coconut oil, sweet almond oil, jojoba oil, beeswax, vitamin E oil, aloe vera gel, essential oils.</p>
      </div>
      <div class="info-block">
        <div class="info-heading">HOW TO USE:</div>
        <p>Apply to dry skin, massage gently, and let it absorb</p>
      </div>
    </div>
    <div class="label-marks">
      <span class="volume">200ML</span>
      <svg class="open-jar-icon" viewBox="0 0 30 30" aria-label="12 months after opening">
        <path d="M4,6 L25,2 L26,6 L5,10 Z" fill="none" stroke="#fff" stroke-width="1.6"/>
        <path d="M4,13 H26 V26 H4 Z" fill="none" stroke="#fff" stroke-width="1.6"/>
        <text x="15" y="23.5" text-anchor="middle" font-size="7" font-weight="600" fill="#fff" font-family="Montserrat, Arial, sans-serif">12M</text>
      </svg>
      <span class="cert-badge" role="img" aria-label="Cruelty free badge"></span>
      <span class="cert-badge" role="img" aria-label="Organic badge"></span>
      <span class="cert-badge" role="img" aria-label="Vegan badge"></span>
    </div>
  </section>

  <section class="label label--mivo">
    <svg class="label-bg" viewBox="0 0 1070 380" preserveAspectRatio="none" aria-hidden="true">
      <path class="swoosh" d="M525,90 C565,30 650,8 730,0 L700,8 C660,20 640,35 628,55 C605,95 625,160 592,232 C550,315 470,345 425,380 L385,380 C470,330 540,290 565,228 C595,160 570,110 588,70 C565,70 540,78 525,90 Z"/>
      <path class="panel" d="M730,0 L1070,0 L1070,380 L425,380 C490,335 570,300 605,225 C640,150 610,85 645,45 C670,15 700,6 730,0 Z"/>
    </svg>
    <div class="label-front">
      <div class="brand-mark"><span class="brand-dot"></span><span class="brand-name">TOLVAREN</span></div>
      <div class="brand-tagline">NATURAL SKINCARE</div>
      <div class="product-band">MIVO</div>
      <div class="product-type">BODY BUTTER</div>
      <div class="product-keys">GUARANA &amp;<br>CUPUAÇU BUTTER</div>
    </div>
    <div class="label-info">
      <div class="info-block">
        <div class="info-heading">INGREDIENTS:</div>
        <p>Shea butter, cocoa butter, cupuaçu butter, guarana extract, coconut oil, sweet almond oil, jojoba oil, bees-wax, vitamin E oil, essential oils</p>
      </div>
      <div class="info-block">
        <div class="info-heading">HOW TO USE:</div>
        <p>Apply to dry skin, massage gently, and let it absorb</p>
      </div>
    </div>
    <div class="label-marks">
      <span class="volume">200ML</span>
      <svg class="open-jar-icon" viewBox="0 0 30 30" aria-label="12 months after opening">
        <path d="M4,6 L25,2 L26,6 L5,10 Z" fill="none" stroke="#fff" stroke-width="1.6"/>
        <path d="M4,13 H26 V26 H4 Z" fill="none" stroke="#fff" stroke-width="1.6"/>
        <text x="15" y="23.5" text-anchor="middle" font-size="7" font-weight="600" fill="#fff" font-family="Montserrat, Arial, sans-serif">12M</text>
      </svg>
      <span class="cert-badge" role="img" aria-label="Cruelty free badge"></span>
      <span class="cert-badge" role="img" aria-label="Organic badge"></span>
      <span class="cert-badge" role="img" aria-label="Vegan badge"></span>
    </div>
  </section>

  <section class="label label--coffee">
    <svg class="label-bg" viewBox="0 0 1070 380" preserveAspectRatio="none" aria-hidden="true">
      <path class="swoosh" d="M525,90 C565,30 650,8 730,0 L700,8 C660,20 640,35 628,55 C605,95 625,160 592,232 C550,315 470,345 425,380 L385,380 C470,330 540,290 565,228 C595,160 570,110 588,70 C565,70 540,78 525,90 Z"/>
      <path class="panel" d="M730,0 L1070,0 L1070,380 L425,380 C490,335 570,300 605,225 C640,150 610,85 645,45 C670,15 700,6 730,0 Z"/>
    </svg>
    <div class="label-front">
      <div class="brand-mark"><span class="brand-dot"></span><span class="brand-name">TOLVAREN</span></div>
      <div class="brand-tagline">NATURAL SKINCARE</div>
      <div class="product-band">COFFEE</div>
      <div class="product-type">BODY SCRUB</div>
      <div class="product-keys">COFFEE AND<br>DEMERARA SUGAR</div>
    </div>
    <div class="label-info">
      <div class="info-block">
        <div class="info-heading">INGREDIENTS:</div>
        <p>Ground coffee, demerara sugar, co-conut oil, sweet almond oil, vitamin E oil, essential oils.</p>
      </div>
      <div class="info-block">
        <div class="info-heading">HOW TO USE:</div>
        <p>Apply to wet skin, massage gently, rinse thoroughly.</p>
      </div>
    </div>
    <div class="label-marks">
      <span class="volume">200ML</span>
      <svg class="open-jar-icon" viewBox="0 0 30 30" aria-label="12 months after opening">
        <path d="M4,6 L25,2 L26,6 L5,10 Z" fill="none" stroke="#fff" stroke-width="1.6"/>
        <path d="M4,13 H26 V26 H4 Z" fill="none" stroke="#fff" stroke-width="1.6"/>
        <text x="15" y="23.5" text-anchor="middle" font-size="7" font-weight="600" fill="#fff" font-family="Montserrat, Arial, sans-serif">12M</text>
      </svg>
      <span class="cert-badge" role="img" aria-label="Cruelty free badge"></span>
      <span class="cert-badge" role="img" aria-label="Organic badge"></span>
      <span class="cert-badge" role="img" aria-label="Vegan badge"></span>
    </div>
  </section>

</main>
</body>
</html>
```